Artwork for Space/Ambient/Drone synthesizer music

Art work is needed for a Collection of ambient type synthesizer soundtrack type of music. Title of album is Drift Logs Vol. 1. This album's theme were to be kept as Movie music & Game music.

Looking for art reminiscent of Rune Halvik retro futuristic look. Open to any ideas but I would like to see primarily sci-fi themes. I would like to have my logo either top center or bottom center and title of album top center or bottom center.

Online distributor requires art to be 2000 x 2000 at minimum but larger is preferable and no bigger than 10mb.

Track list with time is as follows:

1. Far Lantern 05:20
2. Moonwake 10:09
3. Tides 02:31
4. Hush 04:39
5. Paper Tenant 03:55
6. Velvet Echo 03:13
7. Stillwater 03:40
8. Unmoored 06:03
9. Lullabies 02:06

I have uploaded 7 images by Rune Halvik as reference for you (do not use those as I don't have rights to them). My logo is also uploaded for you to use in the art.

Target Market(s)

Synthwave. Retrowave. Ambient/Drone

Industry/Entity Type

Music Download

Font styles to use
Decorative

Colors

Designer to choose colors to be used in the design.

Requirements
Must have
• My logo (provided). Can change color of logo to fit art work.
Nice to have
• Abstract art is welcome.
Should not have
• No drug references. No death references. No references to countries. No graffiti style of art. No vector 80s graphics. No prominent faces. No religious references.

```html
<!DOCTYPE html>
<html lang="en">
<head>
<meta charset="utf-8">
<title>Drift Logs Vol. 1 — Album Cover</title>
<link rel="stylesheet" href="https://fonts.googleapis.com/css2?family=Alfa+Slab+One&display=swap">
<style>
  :root {
    --backdrop: #d3cbb2;
    --cover-dark: #0c0e12;
    --cover-brown: #5a4632;
    --cover-umber: #3a3026;
    --cover-navy: #121a30;
    --cover-blue: #2a3a7a;
    --cover-steel: #5d6864;
    --cover-slate: #3b4545;
    --cover-ash: #8a918a;
    --cover-shadow: #16191b;
    --glow: #c4ceff;
    --title: #f3f0e8;
    --label: #c9b8f0;
  }
  * { margin: 0; padding: 0; box-sizing: border-box; }
  html, body {
    width: 1200px;
    height: 900px;
    overflow: hidden;
    background: var(--backdrop);
  }
  .canvas { position: relative; width: 1200px; height: 900px; }
  .album-cover {
    position: absolute;
    left: 200px;
    top: 50px;
    width: 800px;
    height: 800px;
    overflow: hidden;
    background: var(--cover-dark);
  }
  .cover-art { position: absolute; inset: 0; width: 800px; height: 800px; display: block; }
  .label-name {
    position: absolute;
    top: 118px;
    left: 0;
    width: 100%;
    text-align: center;
    font-family: "Alfa Slab One", serif;
    font-size: 24px;
    letter-spacing: 3px;
    color: var(--label);
    text-transform: uppercase;
  }
  .album-title {
    position: absolute;
    top: 238px;
    left: 0;
    width: 100%;
    text-align: center;
    font-family: "Alfa Slab One", serif;
    font-weight: 400;
    font-size: 46px;
    letter-spacing: 2px;
    color: var(--title);
    text-transform: uppercase;
    white-space: nowrap;
  }
</style>
</head>
<body>
  <main class="canvas">
    <section class="album-cover">
      <svg class="cover-art" viewBox="0 0 800 800" xmlns="http://www.w3.org/2000/svg">
        <defs>
          <linearGradient id="sky-to-ground" x1="0" y1="0" x2="0" y2="1">
            <stop offset="0" stop-color="var(--cover-umber)"/>
            <stop offset="0.3" stop-color="var(--cover-dark)"/>
            <stop offset="0.45" stop-color="var(--cover-navy)"/>
            <stop offset="0.52" stop-color="var(--cover-blue)"/>
            <stop offset="0.62" stop-color="var(--cover-steel)"/>
            <stop offset="0.85" stop-color="var(--cover-slate)"/>
            <stop offset="1" stop-color="var(--cover-steel)"/>
          </linearGradient>
          <linearGradient id="upper-haze" x1="0" y1="0" x2="1" y2="1">
            <stop offset="0" stop-color="var(--cover-brown)" stop-opacity="0"/>
            <stop offset="0.6" stop-color="var(--cover-brown)" stop-opacity="0.7"/>
            <stop offset="1" stop-color="var(--cover-brown)" stop-opacity="0.3"/>
          </linearGradient>
          <linearGradient id="horizon-band" x1="0" y1="0" x2="0" y2="1">
            <stop offset="0" stop-color="var(--cover-blue)" stop-opacity="0"/>
            <stop offset="0.5" stop-color="var(--cover-blue)" stop-opacity="0.9"/>
            <stop offset="1" stop-color="var(--cover-blue)" stop-opacity="0"/>
          </linearGradient>
          <linearGradient id="horizon-glow" x1="0" y1="0" x2="1" y2="0">
            <stop offset="0" stop-color="var(--glow)" stop-opacity="0.3"/>
            <stop offset="0.5" stop-color="var(--glow)" stop-opacity="0.95"/>
            <stop offset="1" stop-color="var(--glow)" stop-opacity="0.6"/>
          </linearGradient>
        </defs>

        <g class="abstract-cityscape" role="img" aria-label="Layered abstract sci-fi cityscape: weathered towers above and below a glowing blue horizon">
          <rect x="0" y="0" width="800" height="800" fill="url(#sky-to-ground)"/>
          <rect x="0" y="0" width="800" height="260" fill="url(#upper-haze)"/>

          <!-- upper structures -->
          <rect class="tower" x="20" y="40" width="110" height="330" fill="var(--cover-umber)" opacity="0.75"/>
          <rect class="tower" x="150" y="20" width="90" height="350" fill="var(--cover-ash)" opacity="0.28"/>
          <rect class="tower" x="255" y="70" width="60" height="300" fill="var(--cover-umber)" opacity="0.6"/>
          <rect class="tower" x="330" y="10" width="14" height="370" fill="var(--cover-ash)" opacity="0.25"/>
          <rect class="slab" x="420" y="150" width="380" height="180" fill="var(--cover-dark)" opacity="0.75"/>
          <rect class="slab-edge" x="420" y="150" width="380" height="4" fill="var(--cover-ash)" opacity="0.25"/>
          <rect class="panel" x="580" y="300" width="220" height="24" fill="var(--cover-blue)" opacity="0.5"/>
          <rect class="panel" x="0" y="330" width="180" height="30" fill="var(--cover-dark)" opacity="0.6"/>

          <!-- horizon -->
          <rect x="0" y="330" width="800" height="110" fill="url(#horizon-band)"/>
          <rect class="skyline-strip" x="0" y="395" width="800" height="26" fill="var(--cover-ash)" opacity="0.45"/>
          <rect class="skyline-strip" x="60" y="382" width="260" height="12" fill="var(--cover-ash)" opacity="0.35"/>
          <rect class="skyline-strip" x="520" y="372" width="230" height="18" fill="var(--cover-ash)" opacity="0.4"/>
          <line x1="0" y1="392" x2="800" y2="352" stroke="url(#horizon-glow)" stroke-width="3"/>
          <line x1="0" y1="428" x2="800" y2="418" stroke="var(--glow)" stroke-width="1" opacity="0.35"/>

          <!-- lower structures -->
          <rect class="ground" x="0" y="440" width="800" height="360" fill="var(--cover-steel)" opacity="0.35"/>
          <rect class="block" x="40" y="470" width="170" height="200" fill="var(--cover-slate)" opacity="0.7"/>
          <rect class="block" x="230" y="450" width="40" height="350" fill="var(--cover-shadow)" opacity="0.65"/>
          <rect class="block" x="300" y="540" width="160" height="70" fill="var(--cover-umber)" opacity="0.6"/>
          <rect class="block" x="420" y="440" width="230" height="360" fill="var(--cover-shadow)" opacity="0.85"/>
          <rect class="block" x="480" y="470" width="60" height="300" fill="var(--cover-dark)" opacity="0.8"/>
          <rect class="block" x="660" y="460" width="140" height="240" fill="var(--cover-ash)" opacity="0.35"/>
          <rect class="block" x="60" y="700" width="300" height="100" fill="var(--cover-shadow)" opacity="0.5"/>
          <line x1="0" y1="620" x2="420" y2="610" stroke="var(--cover-ash)" stroke-width="1" opacity="0.4"/>
          <line x1="650" y1="560" x2="800" y2="556" stroke="var(--cover-ash)" stroke-width="1" opacity="0.4"/>
        </g>
      </svg>
      <div class="label-name">Kestrel Tone</div>
      <h1 class="album-title">Drift Logs Vol. 1</h1>
    </section>
  </main>
</body>
</html>
```